Meridian Prestige Academy needs a Courses Fine Brochure

An unique business school 100% focused on the luxury market that offers programs in NY, L.A., Miami, Paris, Milan, and São Paulo, needs a comprehensive brochure with all your programs.
In two versions, to print and as a web flipping book.
Please find attached two examples of our single program brochures.
PLEASE NOTE THAT ALL UPLOADED MATERIALS ARE SAMPLES OF WHAT WE ALREADY DID, AS SOON AS I´VE CHOSEN A DESIGNER I´LL SEND THE CORRECT FILES, TEXTS AND "SUGGESTED IMAGES".
Updates

Target Market(s)

US students interested in short term programs focused on luxury.
The brochure must display 12 short term programs that will take place in 2017 in Miami, Florida.

Industry/Entity Type

Education

Contact Information for Business Card

Black sober fine finishing business card.
Name, place, phone, address, e-mail, cel.

Font styles to use
Serif
Sans Serif
Script

Requirements
Must have
• Fine finishing, as smooth touch mate lamination, and/or hotstamping, and/or located varnish.
• Easy to read. Every program has Name, brief introduction, date, time, duration, some keynote speaker picture and brief resumé (short cv). And 5 to 10 content topics. Course highlights.
Nice to have
• Luxury products and services. Sofisticated images, closeups and nice views.
• We are talking about teaching luxury for entrepreneurs mainly.
• Business owners or high level executives.
Should not have
• Less is more. Promotional look. Cheap look. Colorful blasting design.

```html
<!DOCTYPE html>
<html lang="en">
<head>
<meta charset="utf-8">
<title>Meridian Prestige Academy – Luxury Hospitality Summit Brochure Cover</title>
<link rel="stylesheet" href="https://fonts.googleapis.com/css2?family=Lobster&family=Open+Sans:wght@400;600&family=Cinzel:wght@400&display=swap">
<style>
  :root {
    --backdrop: #8e8e8e;
    --gold: #b99149;
    --gold-text: #b78d45;
    --ink: #2b2b2b;
    --paper: #ffffff;
    --line: #3a3a3a;
    --sky-top: #2f6fd0;
    --sky-mid: #8fb8e8;
    --water: #2c4d86;
  }
  html, body {
    margin: 0;
    padding: 0;
    width: 1200px;
    height: 880px;
    overflow: hidden;
    background: var(--backdrop);
  }
  .spread {
    position: absolute;
    left: 80px;
    top: 180px;
    width: 1040px;
    height: 520px;
    display: flex;
    box-shadow: 0 10px 30px rgba(0,0,0,0.25);
  }
  .page {
    position: relative;
    width: 520px;
    height: 520px;
    box-sizing: border-box;
  }
  /* Back cover */
  .back-cover {
    background: var(--gold);
    color: var(--paper);
  }
  .brand {
    text-align: center;
    line-height: 1;
  }
  .brand-name {
    font-family: "Lobster", cursive;
    font-size: 40px;
  }
  .brand-tag {
    font-family: "Cinzel", serif;
    font-size: 10px;
    letter-spacing: 2px;
    margin-top: 6px;
  }
  .back-cover .brand {
    position: absolute;
    left: 60px;
    top: 180px;
    width: 400px;
    color: var(--paper);
  }
  .contact-card {
    position: absolute;
    left: 250px;
    top: 300px;
    width: 210px;
    height: 220px;
    background: var(--paper);
    color: var(--ink);
    font-family: "Open Sans", sans-serif;
    font-size: 15px;
    text-align: center;
    padding-top: 16px;
    box-sizing: border-box;
  }
  .contact-item { margin-bottom: 8px; }
  .contact-item svg { display: block; margin: 0 auto 2px; }
  /* Front cover */
  .front-cover {
    background: var(--paper);
  }
  .front-cover .brand {
    position: absolute;
    left: 0;
    top: 28px;
    width: 100%;
    color: var(--gold-text);
  }
  .front-cover .brand-name { font-size: 30px; }
  .front-cover .brand-tag { font-size: 8px; }
  .event-title {
    position: absolute;
    top: 100px;
    width: 100%;
    text-align: center;
    font-family: "Lobster", cursive;
    font-size: 28px;
    color: var(--ink);
  }
  .event-edition {
    position: absolute;
    top: 136px;
    width: 100%;
    text-align: center;
    font-family: "Lobster", cursive;
    font-size: 40px;
    color: var(--gold-text);
  }
  .photo-frame {
    position: absolute;
    left: 20px;
    top: 196px;
    width: 480px;
    height: 230px;
    border-top: 1px solid var(--gold);
    border-bottom: 1px solid var(--gold);
    padding: 6px 0;
  }
  .photo {
    position: relative;
    margin: 0 26px;
    height: 230px;
    background: linear-gradient(180deg, var(--sky-top) 0%, var(--sky-mid) 45%, #c9a88a 55%, var(--water) 72%, #1f3b6a 100%);
  }
  .event-dates {
    position: absolute;
    right: 16px;
    bottom: 40px;
    font-family: "Lobster", cursive;
    font-size: 26px;
    color: var(--paper);
  }
  .event-venue {
    position: absolute;
    right: 16px;
    bottom: 20px;
    font-family: "Open Sans", sans-serif;
    font-size: 13px;
    color: var(--paper);
  }
  .web-rule {
    position: absolute;
    left: 40px;
    top: 458px;
    width: 440px;
    display: flex;
    align-items: center;
    gap: 10px;
    font-family: "Open Sans", sans-serif;
    font-size: 15px;
    color: var(--ink);
  }
  .web-rule::before, .web-rule::after {
    content: "";
    flex: 1;
    height: 1px;
    background: var(--line);
  }
</style>
</head>
<body>
  <main class="spread">
    <section class="page back-cover">
      <div class="brand">
        <div class="brand-name">Meridian Prestige Academy</div>
        <div class="brand-tag">CORPORATE EDUCATION</div>
      </div>
      <div class="contact-card">
        <div class="contact-item">
          <svg width="20" height="20" viewBox="0 0 20 20" aria-hidden="true">
            <circle cx="10" cy="10" r="8.5" fill="none" stroke="#2b2b2b" stroke-width="1.5"/>
            <ellipse cx="10" cy="10" rx="3.5" ry="8.5" fill="none" stroke="#2b2b2b" stroke-width="1.2"/>
            <line x1="1.5" y1="10" x2="18.5" y2="10" stroke="#2b2b2b" stroke-width="1.2"/>
          </svg>
          +1 305 555 0142
        </div>
        <div class="contact-item">
          <svg width="20" height="20" viewBox="0 0 20 20" aria-hidden="true">
            <circle cx="10" cy="10" r="8.5" fill="none" stroke="#2b2b2b" stroke-width="1.5"/>
            <path d="M7 5.5 L8.6 8 L7.6 9 Q9 11.6 11 12.4 L12 11.4 L14.5 13 L13.4 14.6 Q8 14 5.4 6.6 Z" fill="#2b2b2b"/>
          </svg>
          www.meridianprestige.edu
        </div>
        <div class="contact-item">
          <svg width="20" height="20" viewBox="0 0 20 20" aria-hidden="true"><circle cx="10" cy="10" r="8.5" fill="#2b2b2b"/></svg>
          meridianprestige
        </div>
        <div class="contact-item">
          <svg width="20" height="20" viewBox="0 0 20 20" aria-hidden="true"><circle cx="10" cy="10" r="8.5" fill="#2b2b2b"/></svg>
          meridianacademy
        </div>
      </div>
    </section>

    <section class="page front-cover">
      <div class="brand">
        <div class="brand-name">Meridian Prestige Academy</div>
        <div class="brand-tag">CORPORATE EDUCATION</div>
      </div>
      <h1 class="event-title" style="margin:0">IV Luxury Hospitality Summit</h1>
      <div class="event-edition">Miami- 2017</div>
      <div class="photo-frame">
        <div class="photo" role="img" aria-label="Photo of a sunny Miami waterfront with pastel buildings, palm trees, moored boats and a yacht under a blue sky">
          <div class="event-dates">23, 24 and 25 July 2017</div>
          <div class="event-venue">Hotel mane here - Miami</div>
        </div>
      </div>
      <div class="web-rule">www.meridianprestige.edu</div>
    </section>
  </main>
</body>
</html>
```